Business Card Design Project for Harbourlight Homes

We need a business card design for Harbourlight Homes Ltd, a respected building company that specialises in high quality designer homes.

We're after a sleek, clean, modern business card (could even have an interesting shape or something different from normal business cards) with wow factor that people will remember. It also needs to look sharp and great on print.

Please see example attached (do not copy, for inspiration only).

It needs to be in line with the new logo (see attached) and look consistent with that.

The new business card should include the Trusted Trades logo (see attached) as well as the company logo and the two need to look balanced and sleek in regards to their position on the card.
_______________________________________________________
Details to be included:
Tobin Vareck
Director

M: 021 555 0148
E: milo@harbourlighthomes.example
W: www.harbourlighthomes.example

If you present an option for an open card, here's some additional wording we would like you to use:

Harbourlight Homes are a highly skilled team who specialises in residential projects, from simple homes through to top end architectural designs.
We will treat your project with integrity, the attention it deserves, and we guarantee 100% satisfaction.

Timeless craftsmanship. Uncompromising standards.

___________________________________________________________
Additional info on Harbourlight Homes for your consideration:

The core values of the company are integrity, trust, expertise and uncompromising standards.

Harbourlight Homes have been building homes for over 20 years. Only residential, from simple 2-3 bedroom homes through to top end architectural designs. They are a registered Trusted Trade (the Trusted Trades Federation is a highly trusted and respected organisation in New Zealand).

The team at Harbourlight Homes pride themselves in delivering impeccable service to their clients and position themselves as their trusted partners and friends in the construction of their most valuable asset.

Thanks! We look forward to your designs!!!

Target Market(s)

People 30 yrs+ who have an interest in owning quality homes and are prepared to pay for it. Homes built to standards, future-proofed, building savvy.

Industry/Entity Type

Construction

Requirements
Must have
• We're looking for some wow factor as well and something that stands out and people will remember

The final design should communicate timeless craftsmanship, trust, special, VALUE, exquisite, stylish, standing the test of time, no cutting corners, reliability and high standards.

The final design also needs to be sharp and look great on print. The file supplied needs to be high resolution.

```html
<!DOCTYPE html>
<html lang="en">
<head>
<meta charset="utf-8">
<title>Harbourlight Homes Ltd – Folded Business Card</title>
<link rel="stylesheet" href="https://fonts.googleapis.com/css2?family=Lato:wght@400&display=swap">
<style>
  :root {
    --backdrop: #3c3c3e;
    --card-deep: #000000;
    --card-mid: #1c1c1f;
    --card-light: #2a2a2d;
    --ink: #ffffff;
    --ink-soft: #e6e6e6;
    --accent: #d3122a;
    --grain: #4a4846;
    --badge: #f4f4f4;
  }
  * { margin: 0; padding: 0; box-sizing: border-box; }
  html, body {
    width: 1200px; height: 900px; overflow: hidden;
    background: var(--backdrop);
  }
  .canvas { position: relative; width: 1200px; height: 900px; }

  .spread {
    position: absolute; left: 86px; width: 1029px; height: 297px;
    display: flex;
    box-shadow: 0 6px 18px rgba(0,0,0,.45);
  }
  .spread--outside { top: 138px; }
  .spread--inside { top: 464px; }

  .panel { position: relative; width: 50%; height: 100%; }
  .panel--left { background: linear-gradient(90deg, var(--card-deep) 0%, var(--card-mid) 55%, var(--card-light) 100%); }
  .panel--right { background: linear-gradient(90deg, var(--card-deep) 0%, var(--card-mid) 40%, var(--card-light) 100%); }

  .brand { position: absolute; left: 36px; top: 28px; height: 61px; display: flex; align-items: center; }
  .brand__square {
    width: 61px; height: 61px; flex: none;
    background: var(--grain);
  }
  .brand__name {
    margin-left: 16px;
    font-family: "Lato", sans-serif; font-weight: 400; font-size: 24px; line-height: 29px;
    color: var(--ink); letter-spacing: 2px; white-space: nowrap;
  }

  .about {
    position: absolute; left: 35px; top: 62px; width: 325px;
    font-family: "Lato", sans-serif; font-size: 14px; line-height: 19px;
    color: var(--ink);
  }
  .about p { margin-bottom: 14px; }
  .about .about__motto { color: var(--accent); }

  .texture-swatch {
    position: absolute; left: 417px; top: 29px; width: 60px; height: 60px;
    background: var(--grain);
  }
  .member-badge {
    position: absolute; left: 415px; top: 198px; width: 63px; height: 71px;
    background: var(--badge);
  }

  .person {
    position: absolute; left: 47px; top: 218px;
    font-family: "Lato", sans-serif;
  }
  .person__name { font-size: 17px; color: var(--accent); letter-spacing: .3px; }
  .person__role { font-size: 13px; color: var(--ink); margin-top: 1px; }

  .contact-divider {
    position: absolute; left: 242px; top: 219px; width: 1px; height: 55px;
    background: var(--accent);
  }
  .contact {
    position: absolute; left: 255px; top: 214px;
    font-family: "Lato", sans-serif; font-size: 13px; line-height: 19px;
    border-collapse: collapse;
  }
  .contact th { font-weight: 400; text-align: left; color: var(--accent); padding-right: 8px; }
  .contact td { color: var(--ink-soft); }
</style>
</head>
<body>
<main class="canvas">

  <section class="spread spread--outside" aria-label="Card outside">
    <div class="panel panel--left"></div>
    <div class="panel panel--right">
      <div class="brand">
        <div class="brand__square" role="img" aria-label="Dark timber grain swatch"></div>
        <div class="brand__name">HARBOURLIGHT<br>HOMES LTD</div>
      </div>
    </div>
  </section>

  <section class="spread spread--inside" aria-label="Card inside">
    <div class="panel panel--left">
      <div class="about">
        <p>Harbourlight Homes are a highly skilled team who specialises in residential projects, from simple homes through to top end architectural designs.</p>
        <p>We will treat your project with integrity, the attention it deserves, and we guarantee 100% satisfaction.</p>
        <p class="about__motto">Timeless craftsmanship. Uncompromising standards.</p>
      </div>
      <div class="texture-swatch" role="img" aria-label="Dark timber grain swatch"></div>
      <div class="member-badge" role="img" aria-label="Trusted Trades Federation member badge"></div>
    </div>
    <div class="panel panel--right">
      <div class="brand">
        <div class="brand__square"></div>
        <div class="brand__name">HARBOURLIGHT<br>HOMES LTD</div>
      </div>
      <div class="person">
        <div class="person__name">TOBIN VARECK</div>
        <div class="person__role">Director</div>
      </div>
      <div class="contact-divider"></div>
      <table class="contact">
        <tr><th>Mobile:</th><td>021 555 0148</td></tr>
        <tr><th>Email:</th><td>milo@harbourlighthomes.example</td></tr>
        <tr><th>Web:</th><td>www.harbourlighthomes.example</td></tr>
      </table>
    </div>
  </section>

</main>
</body>
</html>
```